Rebrand & reskin trilbodash.com (Uncoded)

Trilbodash.com is a commerce website and app for sports and fitness classes and events. In order to improve its appeal, we invite designers to provide their 'skins' for the landing page, club page and event page. Designers can propose using alternate controls and layouts for these pages, and comment on ways to improve the site's usability. It must remain easy to use on a portrait mobile phone screen, responsive design where necessary to also provide a good experience on desktop.

Please navigate to trilbodash.com and explore the site, and we look forwards to your suggestions!

Target Market(s)

Primary: Tech-savvy mobile users. Secondary: Desktop users

Industry/Entity Type

Health And Wellness

Number of Pages Required

3 page

Font styles to use
Sans Serif

Colors
ffffff
f37122

Requirements
Must have
• This brief is all about changing the look and feel of the site; the winning design will have an immediate 'wow' factor, yet not sacrifice the ease of finding and paying for classes. It must retain the logo, white and orange must be the primary colours used.
Should not have
• The colour palette must remain roughly as is; for example, a very dark site will not appeal.

```html
<!DOCTYPE html>
<html lang="en">
<head>
<meta charset="utf-8">
<title>Trilbodash – Feed</title>
<link rel="stylesheet" href="https://fonts.googleapis.com/css2?family=Montserrat:wght@300;400;500;700&family=Open+Sans:wght@400&display=swap">
<style>
:root{
  --orange:#f37122;
  --orange-light:#f58a38;
  --orange-dark:#ef5f1a;
  --white:#ffffff;
  --page-bg:#f0f0f0;
  --header-bg:#f3f3f3;
  --sidebar:#484852;
  --sidebar-line:#5d5d66;
  --tab-dark:#2e2e30;
  --footer:#2b2b2b;
  --text-dark:#333333;
  --text-mid:#555555;
  --text-soft:#7a7a7a;
  --border:#d6d6d6;
}
*{box-sizing:border-box;margin:0;padding:0}
html,body{width:1200px;height:928px;overflow:hidden}
body{position:relative;background:var(--page-bg);font-family:"Open Sans",sans-serif;color:var(--text-mid)}

.site-header{position:absolute;left:0;top:0;width:1200px;height:102px;background:linear-gradient(#f8f8f8,#ececec);border-bottom:1px solid #cfcfcf}
.brand{position:absolute;left:117px;top:34px;display:flex;align-items:center;gap:10px;font-family:"Montserrat",sans-serif;font-weight:700;font-size:27px;color:var(--orange);letter-spacing:.5px}
.brand-dot{width:26px;height:26px;border-radius:50%;background:var(--orange)}
.main-nav{position:absolute;top:0;left:436px;height:102px;display:flex}
.main-nav a{display:flex;align-items:center;justify-content:center;height:102px;font-family:"Montserrat",sans-serif;font-weight:500;font-size:16.5px;color:#444;text-decoration:none;border-right:1px solid #d4d4d4}
.main-nav a:last-child{border-right:none}
.nav-calendar{width:140px;border-right:none!important}
.nav-feed{width:114px;background:linear-gradient(#444446,#232325);color:var(--white)!important}
.nav-nearby{width:137px}
.nav-classes{width:139px}
.nav-event{width:130px}

.sidebar{position:absolute;left:105px;top:102px;width:223px;height:767px;background:var(--sidebar)}
.side-item{display:flex;align-items:center;height:57px;border-bottom:1px solid var(--sidebar-line);padding-left:28px;font-family:"Montserrat",sans-serif;font-weight:500;font-size:16.5px;color:var(--white)}
.side-item:last-child{border-bottom:none}
.side-item svg{width:28px;height:26px;margin-right:10px;flex:none}

.content{position:absolute;left:328px;top:102px;width:768px;height:767px;background:var(--white)}

.hero{position:absolute;left:22px;top:36px;width:724px;height:270px;overflow:hidden}
.hero-photo{position:absolute;inset:0;background:radial-gradient(ellipse at 55% 60%,#e9d6c8 0%,#eee9e0 45%,#f1efe8 75%,#e6ead8 100%)}
.hero-veil{position:absolute;inset:0;background:rgba(255,255,255,.55)}
.hero-inner{position:relative;text-align:center;padding-top:44px;font-family:"Montserrat",sans-serif}
.hero-title{font-weight:400;font-size:32px;color:var(--text-dark);letter-spacing:.5px}
.hero-sub{font-weight:300;font-size:25px;line-height:30px;color:var(--text-dark);margin:8px 50px 0}
.hero-actions{display:flex;justify-content:center;gap:20px;margin-top:16px}
.btn{width:133px;height:37px;display:flex;align-items:center;justify-content:center;font-size:15px;font-weight:500;color:var(--white)}
.btn-login{background:var(--orange)}
.btn-signup{background:#262626}
.hero-note{margin-top:8px;margin-left:150px;font-size:12.5px;color:#444}

.feed{position:absolute;left:26px;top:337px;width:708px}
.feed-head{height:42px;background:linear-gradient(var(--orange-light),var(--orange-dark));color:var(--white);font-family:"Montserrat",sans-serif;font-weight:500;font-size:17px;display:flex;align-items:center;padding-left:21px}
.event-card{height:138px;border:1px solid var(--border);border-top:none;padding:14px 0 0 24px}
.event-card + .event-card{border-top:1px solid var(--border);margin-left:1px}
.event-date{font-size:15px;color:var(--text-mid)}
.event-row{display:flex;margin-top:12px}
.event-avatar{width:61px;height:61px;border-radius:50%;flex:none;margin-right:13px;margin-left:-2px}
.avatar-club{background:#7a1515;border:2px solid #5a0f0f}
.avatar-photo{background:radial-gradient(circle at 45% 45%,#8a5a40,#c9b7a8 70%,#e8e2dc)}
.event-title{font-size:15.5px;color:var(--orange);margin-top:-3px}
.event-meta{font-size:12.6px;color:var(--text-soft);margin-top:6px;line-height:15px}

.site-footer{position:absolute;left:0;top:869px;width:1200px;height:59px;background:var(--footer);color:#bdbdbd;font-size:14px;display:flex;align-items:center;justify-content:center}
</style>
</head>
<body>

<header class="site-header">
  <div class="brand"><span class="brand-dot"></span>TRILBODASH</div>
  <nav class="main-nav">
    <a class="nav-calendar">CALENDAR</a>
    <a class="nav-feed">FEED</a>
    <a class="nav-nearby">NEAR BY</a>
    <a class="nav-classes">CLASSES</a>
    <a class="nav-event">EVENT</a>
  </nav>
</header>

<aside class="sidebar">
  <div class="side-item">
    <svg viewBox="0 0 28 26"><path d="M2 10h9V5l8 8-8 8v-5H2z" fill="#fff"/><path d="M16 3h7a2 2 0 0 1 2 2v16a2 2 0 0 1-2 2h-7" fill="none" stroke="#fff" stroke-width="2.5"/></svg>
    LOGIN
  </div>
  <div class="side-item">
    <svg viewBox="0 0 28 26"><rect x="4" y="1" width="20" height="24" rx="2" fill="none" stroke="#fff" stroke-width="2.5"/><path d="M9 1v7l2-2 2 2V1" fill="#fff"/><path d="M16 13l1.5 3 3 .4-2.2 2 .6 3-2.9-1.6-2.9 1.6.6-3-2.2-2 3-.4z" fill="#fff"/></svg>
    MY DIARY
  </div>
  <div class="side-item">
    <svg viewBox="0 0 28 26"><path d="M14 0l13 13-13 13L1 13z" fill="#fff"/><rect x="6" y="11.5" width="16" height="3" fill="#484852"/><rect x="7" y="8.5" width="3" height="9" fill="#484852"/><rect x="18" y="8.5" width="3" height="9" fill="#484852"/></svg>
    MY CLUBS
  </div>
  <div class="side-item">
    <svg viewBox="0 0 28 26"><circle cx="14" cy="7" r="6" fill="#fff"/><path d="M2 26v-5a7 7 0 0 1 7-7h10a7 7 0 0 1 7 7v5z" fill="#fff"/></svg>
    MY PROFILE
  </div>
</aside>

<main class="content">
  <section class="hero">
    <div class="hero-photo" role="img" aria-label="Athlete doing a push-up outdoors on a sunny field"></div>
    <div class="hero-veil"></div>
    <div class="hero-inner">
      <h1 class="hero-title">WELCOME TO TRILBODASH</h1>
      <p class="hero-sub">Thanks for visiting! Here are a list of events that we hope are of interest.</p>
      <div class="hero-actions">
        <span class="btn btn-login">LOGIN</span>
        <span class="btn btn-signup">SIGN UP!</span>
      </div>
      <p class="hero-note">Not a member yet?</p>
    </div>
  </section>

  <section class="feed">
    <div class="feed-head">TODAY</div>
    <article class="event-card">
      <div class="event-date">Monday 12th September</div>
      <div class="event-row">
        <div class="event-avatar avatar-club" role="img" aria-label="Club badge"></div>
        <div>
          <div class="event-title">8:15 pm Swim Training</div>
          <div class="event-meta">North Vale Runners @ Elmwood Academy</div>
          <div class="event-meta">Freestyle (crawl) training comprising of warm up, drills and main set.</div>
        </div>
      </div>
    </article>
    <article class="event-card">
      <div class="event-date">Monday 11th September</div>
      <div class="event-row">
        <div class="event-avatar avatar-photo" role="img" aria-label="Photo of an athlete training"></div>
        <div>
          <div class="event-title">9:15 pm Donec dictum lectus</div>
          <div class="event-meta">North Vale Runners @ Elmwood Academy</div>
          <div class="event-meta">Freestyle (crawl) training comprising of warm up, drills and main set.</div>
        </div>
      </div>
    </article>
  </section>
</main>

<footer class="site-footer">© 2016 Company Name&nbsp; All right reserved&nbsp; Term of Use</footer>

</body>
</html>
```